Kelvoran Financial Web Design Contest

We would like for you to design a website for www.kelvoranfinancial.example. Kelvoran Financial is a CPA Firm offering accounting, auditing, and tax preparation services.

We would like to have a consistent feel with the logo, business card, envelope, and stationary designs that were created by another designer on ArtHive. Examples of each are attached. We would like the website to have a clean/modern style.

The website should include the following:

1. A general "Welcome" landing page
2. A "About the Company" page
3. A "Services Offered" page
4. A "Contact Us" form
5. A button for "Sign up for Newsletter"

Target Market(s)

Individuals and businesses that require accounting, auditing, and tax preparation services from a CPA.

Industry/Entity Type

Accounting

Coding

Number of Pages Required

Font styles to use
Other font styles liked:
• Trebuchet or similar

Requirements
Must have
• Consistent feel with logo and letterhead. The gray and blue bar on the letterhead should be incorporated into the website design.

```html
<!DOCTYPE html>
<html lang="en">
<head>
<meta charset="utf-8">
<title>Kelvoran Financial</title>
<link href="https://fonts.googleapis.com/css2?family=Arimo:wght@400;500&family=Ubuntu:wght@300;400&display=swap" rel="stylesheet">
<style>
  :root {
    --navy: #0b2265;
    --charcoal: #4e4e50;
    --button-gray: #7a7a7c;
    --hero-light: #d3dce8;
    --hero-mid: #aebdd2;
    --hero-dark: #8a9cb8;
    --strip: #e6e6ec;
    --ink: #111;
    --white: #fff;
  }
  * { margin: 0; padding: 0; box-sizing: border-box; }
  html, body { width: 1079px; height: 1200px; overflow: hidden; background: var(--white); }
  body { position: relative; font-family: "Arimo", Arial, sans-serif; color: var(--ink); }

  .header-shapes, .footer-shapes { position: absolute; left: 0; width: 1079px; }
  .header-shapes { top: 0; height: 160px; }
  .footer-shapes { top: 1136px; height: 64px; }

  .brand { position: absolute; left: 0; top: 73px; width: 360px; text-align: center; color: var(--white);
    font-family: "Arimo", Arial, sans-serif; font-weight: 400; font-size: 20px; letter-spacing: 0.5px; }

  .phone { position: absolute; left: 709px; top: 29px; font-size: 21px; color: var(--navy); }
  .newsletter-button { position: absolute; left: 875px; top: 28px; width: 171px; height: 25px; background: var(--button-gray); color: var(--white); font-size: 14px; text-align: center; line-height: 25px; }

  .main-nav { position: absolute; top: 104px; left: 0; width: 1079px; font-family: "Ubuntu", sans-serif; font-weight: 300; font-size: 20px; color: var(--white); }
  .main-nav span { position: absolute; transform: translateX(-50%); white-space: nowrap; }

  .hero { position: absolute; left: 0; top: 211px; width: 1079px; height: 400px;
    background: linear-gradient(115deg, var(--hero-dark) 0%, var(--hero-light) 35%, var(--hero-mid) 70%, var(--hero-dark) 100%); }
  .hero-strip { position: absolute; left: 0; top: 611px; width: 1079px; height: 14px; background: var(--strip); }
  .hero-arrow { position: absolute; top: 377px; }
  .hero-caption { position: absolute; left: 212px; top: 332px; width: 645px; height: 187px; background: rgba(255,255,255,0.62); text-align: center; }
  .hero-caption h2 { font-weight: 400; font-size: 18px; margin-top: 30px; }
  .hero-caption p { font-size: 15px; line-height: 21.5px; margin-top: 8px; }
  .learn-more { display: inline-block; margin-top: 10px; width: 113px; height: 25px; line-height: 25px; background: var(--navy); color: var(--white); font-size: 13px; }

  .service { position: absolute; top: 699px; width: 300px; text-align: center; }
  .service-photo { width: 168px; height: 168px; border-radius: 50%; margin: 0 auto; }
  .service h3 { font-weight: 400; font-size: 18px; margin-top: 18px; }
  .service p { font-size: 15px; line-height: 21.4px; margin-top: 16px; }

  .copyright { position: absolute; left: 156px; top: 1170px; font-size: 14px; color: var(--white); }
  .social { position: absolute; top: 1160px; width: 18px; height: 18px; border-radius: 50%; background: var(--white); }
</style>
</head>
<body>
  <svg class="header-shapes" viewBox="0 0 1079 160" aria-hidden="true">
    <polygon points="377,74 1079,74 1079,157 433,157" fill="var(--navy)"/>
    <polygon points="0,15 314,15 404,156 0,156" fill="var(--charcoal)"/>
  </svg>

  <div class="brand">Kelvoran Financial, LLC</div>

  <div class="phone">000-000-0000</div>
  <div class="newsletter-button">Sign up for Newsletter</div>

  <nav class="main-nav">
    <span style="left:515px">HOME</span>
    <span style="left:663px">About Us</span>
    <span style="left:808px">Services</span>
    <span style="left:974px">Contact Us</span>
  </nav>

  <section class="hero" role="img" aria-label="Calculator, coins and financial report pages"></section>
  <div class="hero-strip"></div>
  <svg class="hero-arrow" style="left:35px" width="36" height="82" viewBox="0 0 36 82" aria-hidden="true"><polyline points="35,1 1,41 35,81" fill="none" stroke="#fff" stroke-width="1.5"/></svg>
  <svg class="hero-arrow" style="left:1008px" width="36" height="82" viewBox="0 0 36 82" aria-hidden="true"><polyline points="1,1 35,41 1,81" fill="none" stroke="#fff" stroke-width="1.5"/></svg>

  <div class="hero-caption">
    <h2>Tax preparation services</h2>
    <p>Nunc ac magna. Maecenas odio dolor, vulputate vel, auctor ac, accumsan id,<br>felis. Pellentesque cursus sagittis felis. Pellentesque porttitor, velit lacinia<br>egestas auctor, diam eros tempus arcu, nec vulputate augue magna vel risus.</p>
    <span class="learn-more">Learn More...</span>
  </div>

  <article class="service" style="left:65px">
    <div class="service-photo" role="img" aria-label="Close-up of calculator keys" style="background:radial-gradient(circle at 40% 40%, #c9dbe6, #5d7f94)"></div>
    <h3>Tax preparation services</h3>
    <p>Nunc ac magna. Maecenas odio dolor,<br>vulputate vel, auctor ac, accumsan id,<br>felis. Pellentesque cursus sagittis felis.<br>Pellentesque porttitor, velit lacinia eges-<br>tas auctor, diam eros tempus arcu, nec<br>vulputate augue magna vel risus.</p>
  </article>
  <article class="service" style="left:384px">
    <div class="service-photo" role="img" aria-label="Printed bar and pie charts with a pen" style="background:radial-gradient(circle at 50% 55%, #f1f1f3, #7d7fa8)"></div>
    <h3>Accounting</h3>
    <p>Nunc ac magna. Maecenas odio dolor,<br>vulputate vel, auctor ac, accumsan id,<br>felis. Pellentesque cursus sagittis felis.<br>Pellentesque porttitor, velit lacinia eges-<br>tas auctor, diam eros tempus arcu, nec<br>vulputate augue magna vel risus.</p>
  </article>
  <article class="service" style="left:693px">
    <div class="service-photo" role="img" aria-label="Hands reviewing documents beside a keyboard" style="background:radial-gradient(circle at 45% 45%, #eef0f2, #3d4148)"></div>
    <h3>Auditing</h3>
    <p>Nunc ac magna. Maecenas odio dolor,<br>vulputate vel, auctor ac, accumsan id,<br>felis. Pellentesque cursus sagittis felis.<br>Pellentesque porttitor, velit lacinia eges-<br>tas auctor, diam eros tempus arcu, nec<br>vulputate augue magna vel risus.</p>
  </article>

  <svg class="footer-shapes" viewBox="0 0 1079 64" aria-hidden="true">
    <polygon points="0,18 628,18 594,64 0,64" fill="var(--navy)"/>
    <polygon points="657,4 1079,4 1079,64 607,64" fill="var(--charcoal)"/>
  </svg>
  <div class="copyright">Copyright © 2015 Kelvoran Financial</div>
  <span class="social" style="left:799px" aria-label="Social link"></span>
  <span class="social" style="left:851px" aria-label="Social link"></span>
  <span class="social" style="left:900px" aria-label="Social link"></span>
  <span class="social" style="left:951px" aria-label="Social link"></span>
</body>
</html>
```